Luxury Home Builder looking for an Exciting Homes Portfolio

We have a number of custom homes that we have completed over the years, and we want to give prospective clients are colorful and exciting catalog of our previous homes. I will provide access to the dropbox with all the photos. Need to get as many photos of homes in the catalog as possible. Please use verndalecustomdwell.com for pictures, lots of them in the portfolio, projects in progress, spec homes are available. I will provide full files to the winner. Need a very hip catalog to give out at events, and marketing venues.

Target Market(s)

High Net Worth Individuals looking for luxury homes

Industry/Entity Type

Real Estate Development

Requirements
Must have
• Photos of our project, please use verndalecustomdwell.com to get the photos, and will provide access to full pictures on dropbox to the winner.
• Logo must be incorporated.
Nice to have
• Clarification, website is not for design, but for the purposes of getting the photos. this has to be a very cool portfolio.

```html
<!DOCTYPE html>
<html lang="en">
<head>
<meta charset="utf-8">
<title>Quellmoor – About Spread</title>
<link href="https://fonts.googleapis.com/css2?family=Rubik:wght@400;500;700&display=swap" rel="stylesheet">
<style>
:root{
  --bg:#bdbdbd;
  --page:#f1f1f1;
  --blue:#1d4f8c;
  --text:#6b6b6b;
  --folio:#555555;
}
*{margin:0;padding:0;box-sizing:border-box}
html,body{width:1200px;height:801px;overflow:hidden;background:var(--bg);font-family:"Rubik",sans-serif}
.spread{position:absolute;left:164px;top:252px;width:896px;height:320px;background:var(--page);box-shadow:0 5px 14px rgba(0,0,0,.18)}
.page-text{position:absolute;top:0;height:320px}
.page-left{left:0;width:183px}
.page-right{left:718px;width:178px}
.section-label{position:absolute;top:11px;display:flex;align-items:center;gap:6px;font-size:4.5px;font-weight:700;color:var(--blue);letter-spacing:.2px;line-height:5px}
.section-label .bar{height:5px;background:var(--blue)}
.page-left .section-label{left:8px}
.page-left .section-label .bar{width:48px}
.page-right .section-label{right:0}
.page-right .section-label .bar{width:49px}
.heading{position:absolute;border-left:1.2px solid var(--blue);padding-left:7px;color:var(--blue);font-size:10px;line-height:11px;letter-spacing:.3px}
.heading span{display:block}
.heading .light{font-weight:400}
.heading .bold{font-weight:700}
.heading .medium{font-weight:500}
.body{position:absolute;font-size:4.6px;line-height:6.4px;color:var(--text);text-align:justify}
.body p+p{margin-top:5px}
.services{position:absolute;left:16px;top:126px;list-style:none;font-size:3.9px;line-height:7px;color:var(--blue)}
.services li::before{content:"";display:inline-block;width:1.6px;height:1.6px;background:var(--blue);border-radius:50%;margin-right:4px;vertical-align:middle}
.icon{position:absolute;width:60px;text-align:center;font-size:3.8px;font-weight:700;color:var(--blue);line-height:4px}
.icon svg{display:block;margin:0 auto 10px}
.folio{position:absolute;top:306px;font-size:4.5px;color:var(--folio)}
.photo{position:absolute}
.main-photo{left:183px;top:0;width:535px;height:216px;background:linear-gradient(180deg,#3a78c8 0%,#7fb0e0 30%,#e4ebee 52%,#5a6f4e 82%,#8b8f8a 100%)}
.thumb{top:221px;height:99px}
.t1{left:185px;width:105px;background:linear-gradient(180deg,#5f97d6 0%,#b5a793 50%,#3f5c35 100%)}
.t2{left:293px;width:106px;background:linear-gradient(180deg,#6ea5e2 0%,#d6c7a6 45%,#4f8a3a 100%)}
.t3{left:402px;width:100px;background:linear-gradient(180deg,#3f5a3b 0%,#b88a6a 45%,#8a7766 100%)}
.t4{left:506px;width:104px;background:linear-gradient(180deg,#6aa0d8 0%,#5f7550 45%,#9a8c7c 100%)}
.t5{left:613px;width:105px;background:linear-gradient(180deg,#78a9d9 0%,#3d6434 45%,#7c6f5e 100%)}
</style>
</head>
<body>
<div class="spread">

  <section class="page-text page-left">
    <div class="section-label"><span class="bar"></span>ABOUT QUELLMOOR</div>

    <h2 class="heading" style="left:26px;top:41px"><span class="light">WHO</span><span class="bold">WE ARE</span></h2>
    <div class="body" style="left:26px;top:72px;width:142px">
      <p>At Quellmoor, there are no easy answers, no pat formulas. We leave that sort of thing to the mass market developers. Each home we undertake is a one-of-a-kind, fully customized residence, designed to meet the specific desires of its residents. When you work with a limited universe of prospective clients, there is no room for error. Every home we Design-Build must measure up on every count.</p>
      <p>Because we know that our clients, our homebuyers, serve as our salespeople. Indeed, they are the only 'sales force' we have. They're the best measure of how well we deliver on our promises. We urge anyone interested in the prospect of working with us, to talk to those who have relied on us in the past to create their homes.</p>
    </div>

    <h2 class="heading" style="left:26px;top:186px"><span class="light">OUR</span><span class="bold">GOAL</span></h2>
    <div class="body" style="left:26px;top:219px;width:142px">
      <p>Quellmoor Inter-Development, Inc. is different from other builders because we are a Design-Build company, where every project we undertake is centered on the principle of listening to our clients in order to understand their needs, and on honesty and transparency from start to finish. We take the time to listen to our clients in order to create a custom home that is true to their vision. Quellmoor team works with our clients in open collaboration on every aspect of the build. Every Quellmoor home is a statement about who our clients are and about who we are.</p>
    </div>

    <span class="folio" style="left:26px">3</span>
  </section>

  <div class="photo main-photo" role="img" aria-label="Photo of a white tropical-modern custom home with palm trees and a paved entry walk"></div>
  <div class="photo thumb t1" role="img" aria-label="Photo of a Mediterranean villa with tall cypress trees"></div>
  <div class="photo thumb t2" role="img" aria-label="Photo of a Mediterranean estate with a manicured lawn and flower beds"></div>
  <div class="photo thumb t3" role="img" aria-label="Photo of a courtyard entry with a fountain"></div>
  <div class="photo thumb t4" role="img" aria-label="Photo of a villa with palms and a paver driveway"></div>
  <div class="photo thumb t5" role="img" aria-label="Photo of a gated driveway framed by tropical trees"></div>

  <section class="page-text page-right">
    <div class="section-label">ABOUT QUELLMOOR<span class="bar"></span></div>

    <h2 class="heading" style="left:14px;top:41px"><span class="medium">WHAT MAKES</span><span class="bold">US DIFFERENT</span></h2>
    <div class="body" style="left:14px;top:72px;width:142px">
      <p>We bring our vast experience spanning the entire gamut of real estate services to our clients. It is this experience that permits us to offer an exclusive Quellmoor advantage, the full package of residential construction services in-house. From the very infancy of a project, we assist our clients with every selection necessary to complete the project from start through completion. The following in-house services is what makes Quellmoor a totally different company from others.</p>
    </div>

    <ul class="services">
      <li>All Preliminary Project Analysis</li>
      <li>Square Footage Assessment</li>
      <li>Architectural Programming and Design</li>
      <li>3D Renderings</li>
      <li>Plans Processing</li>
      <li>Permitting</li>
      <li>Land Acquisition</li>
      <li>Site Analysis</li>
      <li>Purchasing Assistance</li>
      <li>Sub-contracts Assistance</li>
      <li>Negotiated Materials and Supplies</li>
      <li>Construction Financing Assistance</li>
      <li>Lending Institution Liaison</li>
    </ul>

    <div class="icon" style="left:5px;top:226px">
      <svg width="18" height="18" viewBox="0 0 24 24"><circle cx="12" cy="12" r="10" fill="var(--blue)"/><path d="M8 12l3 3 5-6" stroke="#fff" stroke-width="2" fill="none"/></svg>
      IN-HOUSE SERVICES
    </div>
    <div class="icon" style="left:56px;top:226px">
      <svg width="18" height="18" viewBox="0 0 24 24"><path d="M2 12L12 3l10 9h-3v10H5V12z" fill="var(--blue)"/><rect x="10" y="15" width="4" height="7" fill="#fff"/></svg>
      EXPERIENCE
    </div>
    <div class="icon" style="left:107px;top:226px">
      <svg width="18" height="18" viewBox="0 0 24 24"><path d="M12 2l2.9 6 6.6.8-4.9 4.5 1.3 6.5L12 16.6 6.1 19.8l1.3-6.5L2.5 8.8 9.1 8z" fill="var(--blue)"/></svg>
      QUALITY AND VALUE
    </div>
    <div class="icon" style="left:24px;top:264px">
      <svg width="18" height="18" viewBox="0 0 24 24"><path d="M5 11L12 4l7 7h-2v6H7v-6z" fill="var(--blue)"/><path d="M2 18q10 6 20 0" stroke="var(--blue)" stroke-width="2" fill="none"/></svg>
      CUSTOMIZATION
    </div>
    <div class="icon" style="left:74px;top:264px">
      <svg width="18" height="18" viewBox="0 0 24 24"><circle cx="12" cy="12" r="9" fill="none" stroke="var(--blue)" stroke-width="2"/><path d="M12 6v6l4 3" stroke="var(--blue)" stroke-width="2" fill="none"/></svg>
      BUDGET AND SCHEDULE
    </div>

    <span class="folio" style="right:20px">4</span>
  </section>

</div>
</body>
</html>
```